Lanterns on the Tide

I need a book cover design for a world history book written for a target audience of high school students and progressive teachers. The book is more balanced towards a world history perspective than a Western-leaning perspective. The first 500 pages deal with the major turning points in world history - from the first hominids that roamed Africa to the end of the Cold War, and the final 100 pages cover the major challenges facing the world today. The book is 95% graphic details, hopefully-engaging stories and needed facts, but there is a bit of sarcasm, verbal irony and asides thrown in to keep the reader's eyes from glossing over. I would need a cover that would appeal to any school teacher, but something that would not scare off students or the average Joe off the street.
Updates

One added note, please leave the bottom right corner -  2" height by 3" width free of text/image for the ISBN code.

As far as a central image goes, it needs to be a dynamic (avoid something readers would readily see elsewhere in their lives) image, or nothing at all.  Also, please justify all text on the back cover to the left side (avoid centering).

Reason: A few people have voiced an interest in having the deadline extended through next weekend to allow for some alterations and also the ability to take advantage of the upcoming holidays. I will take you up on this request. Thank you all again for your submissions. i've seen some very unique takes on the story/tone of the book.

Industry/Entity Type

High School

Requirements
Must have
• I've enclosed a PDF with the text for the front and back cover.

On the back cover, I'd like the quote and the initial question to stand out. I'd like the initial question to be in lower case.

For the spine, I'd like the title font to match the title front from the front cover.

The book cover needs to measure 9.25" by 13.75" with a 1.5" spine. Allow .125 inches for the bleed.

I've attached a Word Document with all the text. The layout is just a suggestion.
Should not have
• I do not want any stock images that I'll need to pay for.

```html
<!DOCTYPE html>
<html lang="en">
<head>
<meta charset="utf-8">
<title>Lanterns on the Tide — Book Cover</title>
<link href="https://fonts.googleapis.com/css2?family=Anton&family=Nunito:wght@900&family=Tinos:ital,wght@0,400;1,700&family=Carlito&display=swap" rel="stylesheet">
<style>
  :root{
    --red-deep:#c81a1f;
    --red:#e0262a;
    --crimson:#b3153a;
    --magenta:#c01f5e;
    --pink:#e4406a;
    --orange:#e8632a;
    --ink:#111111;
    --paper:#ffffff;
    --subtitle:#1d1416;
  }
  *{box-sizing:border-box;margin:0;padding:0}
  html,body{width:1200px;height:728px;overflow:hidden;background:#fff}
  .cover{position:relative;width:1200px;height:728px;overflow:hidden}

  .pattern{position:absolute;top:0;height:728px}
  .pattern--back{left:0;width:548px;
    background:
      radial-gradient(circle at 20% 30%, rgba(232,99,42,.35), transparent 45%),
      radial-gradient(circle at 80% 75%, rgba(179,21,58,.4), transparent 50%),
      linear-gradient(160deg,var(--red) 0%,var(--red-deep) 55%,var(--crimson) 100%);}
  .pattern--spine{left:548px;width:110px;background:linear-gradient(180deg,var(--red-deep),#b8151c)}
  .pattern--front{left:658px;width:542px;
    background:
      radial-gradient(circle at 85% 15%, rgba(228,64,106,.55), transparent 45%),
      radial-gradient(circle at 10% 70%, rgba(232,99,42,.45), transparent 40%),
      radial-gradient(circle at 70% 90%, rgba(179,21,58,.5), transparent 45%),
      linear-gradient(150deg,var(--red) 0%,var(--magenta) 50%,var(--pink) 100%);}
  .fold{position:absolute;top:0;width:1px;height:728px;background:rgba(0,0,0,.35)}

  /* back cover */
  .back-question{position:absolute;left:90px;top:42px;width:440px;text-align:center;
    font-family:"Nunito",sans-serif;font-weight:900;font-size:27px;line-height:34px;color:var(--paper)}
  .back-copy{position:absolute;left:72px;width:470px;font-family:"Tinos",serif;font-size:15.3px;line-height:20.5px;color:var(--paper)}
  .back-copy--one{top:135px}
  .back-copy--two{top:258px}
  .back-copy--three{top:420px}
  .endorsement{position:absolute;left:68px;top:542px;width:345px;
    font-family:"Tinos",serif;font-style:italic;font-weight:700;font-size:15.5px;line-height:20.5px;color:var(--paper)}
  .endorsement cite{font-style:normal;font-weight:400}

  /* spine */
  .spine-title,.spine-author{position:absolute;writing-mode:vertical-rl;white-space:nowrap;font-family:"Anton",sans-serif;letter-spacing:1px}
  .spine-title{left:556px;top:16px;font-size:54px;line-height:62px;color:var(--paper);text-shadow:4px 3px 0 var(--ink)}
  .spine-author{left:622px;top:452px;font-size:36px;line-height:40px;color:var(--ink);text-shadow:2px 2px 0 rgba(255,255,255,.8)}

  /* front cover */
  .front-title{position:absolute;left:700px;top:52px;font-family:"Anton",sans-serif;font-size:112px;line-height:128px;
    color:var(--paper);letter-spacing:1px;text-shadow:6px 5px 0 var(--ink)}
  .front-title span{display:block}
  .front-title .indent-1{padding-left:0}
  .front-title .indent-2{padding-left:90px}
  .front-subtitle{position:absolute;left:720px;top:440px;width:470px;text-align:center;
    font-family:"Carlito",sans-serif;font-size:25px;line-height:28px;color:var(--subtitle)}
  .front-author{position:absolute;left:838px;top:676px;font-family:"Anton",sans-serif;font-size:38px;line-height:44px;
    color:var(--paper);letter-spacing:1px;text-shadow:3px 3px 0 var(--ink)}
</style>
</head>
<body>
<main class="cover">
  <div class="pattern pattern--back" role="img" aria-label="Interlocking jigsaw puzzle pieces in reds and oranges"></div>
  <div class="pattern pattern--spine" role="img" aria-label="Jigsaw puzzle pieces in deep red"></div>
  <div class="pattern pattern--front" role="img" aria-label="Interlocking jigsaw puzzle pieces in reds, pinks and magentas"></div>
  <div class="fold" style="left:548px"></div>
  <div class="fold" style="left:658px"></div>

  <section class="back">
    <h2 class="back-question">do you have any idea<br>how we got to here?</h2>
    <p class="back-copy back-copy--one">Well, if you’re like 97.4% of the people walking the planet, you haven’t got a clue.&nbsp; Sure, you might know a bit about a couple rivers in Mesopotamia, how Socrates wandered around Athens asking questions or how Martin Luther got ticked off one day and nailed a really long essay to the door of a church.&nbsp; But to be honest (and don’t be embarrassed), you’ve got some gaps.</p>
    <p class="back-copy back-copy--two">Be dense no more. In <i>Lanterns on the Tide</i>, Marcus Halloway takes you through all the major tales, traditions and turning points of world history – not just European history, but WORLD history.&nbsp; You’ll figure out real quick that the West might have had some crowning moments, but for the whole of human history, it’s been the Persians, the Indians, the Chinese, the Muslims or some horse peoples from the steppe that have truly turned us into the clever little creatures we are today.</p>
    <p class="back-copy back-copy--three">And when most world history books fade off once the Cold War comes to a close, this sometimes cheekily-written tome just gets going.&nbsp; It finishes with a distinctively comprehensive look at the 21st century challenges facing the nine major regions of today’s world – Africa, Latin America, Japan, China, the Middle East, India, Russia, Europe and the United States.</p>
    <blockquote class="endorsement">“Marcus Halloway expertly understands exactly what his audience wants to know, what they need to know.&nbsp; A page-turning account of our proudest achievements and our most colossal bumblings. It’s world history for the rest of us.” <cite>– Rafiq al-Noor</cite></blockquote>
  </section>

  <section class="spine">
    <p class="spine-title">LANTERNS ON THE TIDE</p>
    <p class="spine-author">MARCUS HALLOWAY</p>
  </section>

  <section class="front">
    <h1 class="front-title"><span class="indent-1">LANTERNS</span><span class="indent-2">ON THE</span><span class="indent-2">TIDE</span></h1>
    <p class="front-subtitle">The tales, traditions and<br>turning points of world history<br>and the regional challenges of today</p>
    <p class="front-author">MARCUS HALLOWAY</p>
  </section>
</main>
</body>
</html>
```